Marnie Vale Photography needs a unique, creative business card/logo design

I need a design for business cards/logo that is unique and creative in the industry. Simplicity is nice, so not too crowded. Something that will catch my customer's eye and remain in their memory. I am primarily a landscape photographer but will be soon may be branching into boudoir photography as well. I have attached my current card.

Marnie Vale Photography
Phone: 0439 517 264
Email: MarnieValePhotography@quillmail.example
Website: www.snapnook.example/MarnieValePhotography.Aust

Marnie Vale Photography

• Contact Details on one side
• pixelation

```html
<!DOCTYPE html>
<html lang="en">
<head>
<meta charset="utf-8">
<title>Marnie Vale Photography – Business Card</title>
<link rel="stylesheet" href="https://fonts.googleapis.com/css2?family=Bangers&family=Libre+Baskerville:ital@1&display=swap">
<style>
  :root {
    --paper: #ffffff;
    --aqua: #5ff0fb;
    --slate: #b5c2c2;
    --ink: #111111;
    --camera-tone: #1c1c1c;
  }
  html, body {
    margin: 0;
    padding: 0;
    width: 1200px;
    height: 702px;
    overflow: hidden;
    background: var(--paper);
  }
  .business-card {
    display: block;
    width: 1200px;
    height: 702px;
  }
  .card-bg { fill: var(--paper); }
  .corner-aqua { fill: var(--aqua); }
  .corner-slate { fill: var(--slate); }
  .brand-name {
    font-family: "Bangers", "Arial Narrow", sans-serif;
    font-size: 112px;
    fill: var(--aqua);
  }
  .contact-line {
    font-family: "Libre Baskerville", Georgia, serif;
    font-style: italic;
    fill: var(--ink);
  }
  .contact-main { font-size: 28px; }
  .contact-web { font-size: 21px; }
  .camera-illustration { fill: var(--camera-tone); }
</style>
</head>
<body>
<svg class="business-card" viewBox="0 0 1200 702" xmlns="http://www.w3.org/2000/svg" aria-labelledby="card-title">
  <title id="card-title">Marnie Vale Photography business card</title>
  <rect class="card-bg" x="0" y="0" width="1200" height="702"/>

  <!-- top-right corner frame -->
  <g class="corner-frame corner-top-right">
    <rect class="corner-aqua" x="906" y="58" width="241" height="25"/>
    <rect class="corner-aqua" x="1111" y="58" width="36" height="244"/>
    <rect class="corner-slate" x="867" y="83" width="241" height="28"/>
    <rect class="corner-slate" x="1061" y="83" width="47" height="247"/>
  </g>

  <!-- bottom-left corner frame -->
  <g class="corner-frame corner-bottom-left">
    <rect class="corner-aqua" x="59" y="402" width="41" height="246"/>
    <rect class="corner-aqua" x="59" y="617" width="241" height="31"/>
    <rect class="corner-slate" x="98" y="376" width="46" height="244"/>
    <rect class="corner-slate" x="98" y="587" width="241" height="33"/>
  </g>

  <text class="brand-name" x="211" y="211" textLength="783" lengthAdjust="spacingAndGlyphs">MARNIE VALE PHOTOGRAPHY</text>

  <rect class="camera-illustration" x="724" y="284" width="258" height="194" rx="60"
        role="img" aria-label="Black ink illustration of a camera with a large lens"/>

  <g class="contact-details">
    <text class="contact-line contact-main" x="148" y="467">PHONE: 0439 517 264</text>
    <text class="contact-line contact-main" x="148" y="517">EMAIL: MarnieValePhotography@quillmail.example</text>
    <text class="contact-line contact-web" x="148" y="561" textLength="980" lengthAdjust="spacingAndGlyphs">WEBSITE: WWW.SNAPNOOK.EXAMPLE/MARNIEVALEPHOTOGRAPHY.AUST</text>
  </g>
</svg>
</body>
</html>
```